Brisk Nova residential and commercial cleaning

We need a Business card design for a new residential and commercial cleaning company based in UAE- Abu Dhabi named (BRISK NOVA)
we provide a residential cleaning service based in hourly rate (Maid Rent - Baby Setting), Also a commercial and offices cleaning.
Our logo is attached for your reference

Target Market(s)

Women who are 22 to 60 years old.

Industry/Entity Type

Residential

Requirements
Should not have
• it should not have an old-style fonts

```html
<!DOCTYPE html>
<html lang="en">
<head>
<meta charset="utf-8">
<title>Brisk Nova – Business Card</title>
<link href="https://fonts.googleapis.com/css2?family=Arimo:wght@400;700&family=Indie+Flower&display=swap" rel="stylesheet">
<style>
  :root {
    --page-bg: #e9e7e3;
    --card-top: #ffffff;
    --card-bottom: #e6e8e9;
    --brand-blue: #1f6fd1;
    --text-blue: #2a63c9;
    --icon-blue: #2f5fae;
    --leaf-green: #8fdc2a;
    --leaf-green-dark: #4fae1e;
  }
  html, body {
    margin: 0;
    width: 1200px;
    height: 900px;
    overflow: hidden;
    background: var(--page-bg);
  }
  .business-card {
    position: absolute;
    left: 100px;
    top: 165px;
    width: 1000px;
    height: 570px;
    background: linear-gradient(180deg, var(--card-top) 0%, var(--card-top) 40%, var(--card-bottom) 100%);
    box-shadow: 0 12px 40px rgba(0,0,0,0.18);
    overflow: hidden;
    font-family: "Arimo", Arial, sans-serif;
  }
  .brand {
    position: absolute;
    left: 0;
    right: 0;
    top: 95px;
    display: flex;
    justify-content: center;
    align-items: center;
    gap: 22px;
  }
  .brand-name {
    font-family: "Arimo", Arial, sans-serif;
    font-weight: 700;
    font-size: 68px;
    color: var(--brand-blue);
    letter-spacing: -1px;
  }
  .brand-mark {
    width: 110px;
    height: 110px;
    border-radius: 50%;
    border: 6px solid var(--leaf-green);
    box-sizing: border-box;
  }
  .holder-name {
    position: absolute;
    left: 0;
    right: 0;
    top: 255px;
    text-align: center;
    font-family: "Indie Flower", "Comic Sans MS", cursive;
    font-size: 58px;
    color: var(--text-blue);
    text-shadow: 1px 2px 2px rgba(0,0,0,0.2);
  }
  .contact {
    position: absolute;
    display: flex;
    flex-direction: column;
    gap: 22px;
  }
  .contact-left { left: 245px; top: 410px; }
  .contact-right { left: 590px; top: 360px; }
  .contact-item {
    display: flex;
    align-items: center;
    gap: 14px;
    font-size: 27px;
    color: var(--text-blue);
  }
  .contact-item svg { width: 34px; height: 34px; flex: none; }
  .sprout {
    position: absolute;
    left: 18px;
    bottom: 22px;
    width: 110px;
    height: 95px;
    border-radius: 40% 50% 30% 50%;
    background: radial-gradient(circle at 50% 45%, var(--leaf-green) 0%, var(--leaf-green-dark) 70%, rgba(79,174,30,0) 100%);
  }
  .footer-band {
    position: absolute;
    left: 0;
    right: 0;
    bottom: 0;
    height: 16px;
    display: flex;
  }
  .footer-band .band-blue { flex: 0 0 52%; background: var(--brand-blue); }
  .footer-band .band-green { flex: 1; background: var(--leaf-green); }
</style>
</head>
<body>
  <main class="business-card">
    <header class="brand">
      <span class="brand-name">Brisk Nova</span>
      <span class="brand-mark"></span>
    </header>

    <div class="holder-name">Name Surname</div>

    <ul class="contact contact-right" style="margin:0;padding:0;list-style:none">
      <li class="contact-item">
        <svg viewBox="0 0 24 24" aria-hidden="true"><path fill="var(--icon-blue)" d="M6.6 2.5l3 3.2-1.8 2.4c1 2.6 3.4 5.2 6.1 6.3l2.4-1.8 3.2 3-2 3c-7.4-.6-13.3-6.6-13.9-14z"/></svg>
        <span>Phone number</span>
      </li>
      <li class="contact-item">
        <svg viewBox="0 0 24 24" aria-hidden="true"><circle cx="12" cy="12" r="10.5" fill="var(--icon-blue)"/><g fill="none" stroke="#fff" stroke-width="1.2"><ellipse cx="12" cy="12" rx="4.5" ry="10.5"/><path d="M1.5 12h21M3 7h18M3 17h18M12 1.5v21"/></g></svg>
        <span>Web</span>
      </li>
    </ul>

    <ul class="contact contact-left" style="margin:0;padding:0;list-style:none">
      <li class="contact-item">
        <svg viewBox="0 0 24 24" aria-hidden="true"><path fill="var(--icon-blue)" d="M12 1.5a7.5 7.5 0 0 0-7.5 7.5c0 5.6 7.5 13.5 7.5 13.5s7.5-7.9 7.5-13.5A7.5 7.5 0 0 0 12 1.5z"/><circle cx="12" cy="9" r="3" fill="#fff"/></svg>
        <span>Adress</span>
      </li>
      <li class="contact-item">
        <svg viewBox="0 0 24 24" aria-hidden="true"><rect x="1.5" y="4.5" width="21" height="15" fill="var(--icon-blue)"/><path d="M1.5 4.5l10.5 9 10.5-9M1.5 19.5l8-7M22.5 19.5l-8-7" fill="none" stroke="#fff" stroke-width="1.3"/></svg>
        <span>E-mail</span>
      </li>
    </ul>

    <div class="sprout" role="img" aria-label="Small green leafy sprout illustration"></div>

    <div class="footer-band">
      <span class="band-blue"></span>
      <span class="band-green"></span>
    </div>
  </main>
</body>
</html>
```